Business Card Design For Bluepine Audio

Bluepine Audio is a small pro-audio company providing rental and install services for professional sound reinforcement. Focus is gigs (any gigs) needing high quality audio; from corporate to chamber music to hard hitting rock.

Bluepine Audio
Pro-audio for your gig ... spine-tingle grand
Corin Halsey
corin@bluepineaudio.com.au
0438 562 071

We need a business card design and an "drop-off"' larger card (eg. one third A4 size: 99mm wide x 210mm high) with more details.
Updates

Please note I've had limited internet access for last few days and for the next four.  The work so far looks great .. I'll provide some individual feedback on the designs now.  Great work, many thanks, love the creativity!

Corin

Industry/Entity Type

Business

```html
<!DOCTYPE html>
<html lang="en">
<head>
<meta charset="utf-8">
<title>Bluepine Audio — Business Card</title>
<link rel="stylesheet" href="https://fonts.googleapis.com/css2?family=Chelsea+Market&display=swap">
<style>
  :root {
    --ink: #141210;
    --salmon: #f0907c;
    --orange: #f3a43c;
    --gold: #e8c846;
    --lime: #c9de4e;
    --leaf: #93d46c;
    --green: #3fc07a;
    --teal: #13a08c;
  }
  html, body {
    margin: 0;
    padding: 0;
    width: 1200px;
    height: 693px;
    overflow: hidden;
    background: #ffffff;
  }
  .card {
    position: relative;
    width: 1200px;
    height: 693px;
    overflow: hidden;
    background: linear-gradient(118deg,
      var(--salmon) 0%,
      var(--orange) 24%,
      var(--gold) 40%,
      var(--lime) 52%,
      var(--leaf) 64%,
      var(--green) 80%,
      var(--teal) 100%);
  }
  .card-type {
    position: absolute;
    inset: 0;
    width: 1200px;
    height: 693px;
    font-family: "Chelsea Market", Georgia, serif;
    fill: var(--ink);
  }
  .brand-name { font-size: 128px; }
  .tagline { font-size: 40px; }
  .contact-name { font-size: 80px; }
  .contact-email, .contact-phone { font-size: 52px; }
</style>
</head>
<body>
  <main class="card">
    <svg class="card-type" viewBox="0 0 1200 693" role="group" aria-label="Bluepine Audio business card">
      <text class="brand-name" x="46" y="202" textLength="1100" lengthAdjust="spacingAndGlyphs">Bluepine Audio</text>
      <text class="tagline" x="251" y="240" textLength="898" lengthAdjust="spacingAndGlyphs">Pro-audio for your gig ... spine-tingle grand</text>
      <text class="contact-name" x="308" y="519" textLength="583" lengthAdjust="spacingAndGlyphs">Corin Halsey</text>
      <text class="contact-email" x="178" y="580" textLength="844" lengthAdjust="spacingAndGlyphs">corin@bluepineaudio.com.au</text>
      <text class="contact-phone" x="438" y="638" textLength="322" lengthAdjust="spacingAndGlyphs">0438 562 071</text>
    </svg>
  </main>
</body>
</html>
```